Website Design for Camp 3874

We need a website design for a new company that strives to provide training and structure for religious missionaries who are traveling the world to teach of christianity.
They provide training in:
- Nutrition Coaching & Daily assignments
- Personal Training Sessions
- Phycological emotional/mental component
The goal of Camp 3874 is to help missionaries preach the gospel of christ to those who haven't heard it due to geographical obstacles and physical limitations that get in the way.
The homepage template has linked images to use. If any other images are needed, stock images are acceptable.

Logo/Color Scheme: https://files.nervalo.example/folders/8Kp2QwZr7LmXv4TsN9bHc3YdJ6fGaE1Ru?share=open

Customer Avatar/Core Message Canvas: https://sheets.nervalo.example/s/d/7Hq39TbWmuKpZr2LxNcV8yEs5DfGa4JkQo1BnXtYRMwP/edit?share=open

Homepage Template: https://pages.nervalo.example/doc/d/5nRZ82kLp94QsWxTy7mBuVhCe3DjFa6Go0PiKqNr4Ytw/edit?share=open

```html
<!DOCTYPE html>
<html lang="en">
<head>
<meta charset="utf-8">
<title>Camp 3874 — Missionary Training</title>
<link href="https://fonts.googleapis.com/css2?family=Rajdhani:wght@600;700&family=Roboto:wght@400;500;700&display=swap" rel="stylesheet">
<style>
:root{
  --green:#2c3718;
  --green-deep:#26301a;
  --gold:#e2b83b;
  --gold-soft:#e8c453;
  --ink:#1e1e1e;
  --text:#555;
  --light:#efefef;
  --white:#fff;
}
*{box-sizing:border-box;margin:0;padding:0}
html,body{width:1200px;height:4184px;overflow:hidden}
body{font-family:"Roboto",Arial,sans-serif;color:var(--ink);background:var(--white)}
.heading{font-family:"Rajdhani","Arial Narrow",sans-serif;font-weight:700;letter-spacing:1.5px;text-transform:uppercase}
a{text-decoration:none;color:inherit}
.btn{display:inline-flex;align-items:center;gap:10px;font-size:15px;font-weight:700;text-transform:uppercase;padding:0 22px;height:46px;border-radius:6px}
.btn svg{width:15px;height:15px}
.btn-green{background:var(--green);color:var(--white)}
.btn-gold{background:var(--gold);color:var(--white)}
.btn-outline{border:2px solid var(--white);color:var(--white)}

/* header */
.site-header{height:91px;display:flex;align-items:center;padding:0 110px;justify-content:space-between}
.brand{display:flex;align-items:center;gap:10px}
.brand-name{font-family:"Rajdhani",sans-serif;font-weight:700;font-size:46px;color:var(--green);letter-spacing:1px}
.brand-mark{width:36px;height:36px;background:var(--gold);border-radius:6px}
.main-nav{display:flex;gap:38px;font-size:15px;color:#333;margin-left:auto;margin-right:28px}
.signup{height:46px;padding:0 22px;font-size:15px}

/* hero */
.hero{position:relative;height:640px;background:linear-gradient(180deg,#7e95ab 0%,#a8b3ba 30%,#6c5f4d 62%,#4a3b2a 100%);color:var(--white);text-align:center}
.hero-inner{position:absolute;left:0;right:0;top:236px}
.hero h1{font-size:35px;line-height:41px;text-shadow:0 2px 6px rgba(0,0,0,.5)}
.hero p{font-size:15px;line-height:26px;width:660px;margin:24px auto 0;font-weight:500}
.hero-actions{display:flex;justify-content:center;gap:16px;margin-top:24px}

/* staff */
.staff{height:786px;padding-top:97px;text-align:center}
.section-title{font-size:34px;line-height:37px;color:var(--ink)}
.staff-grid{display:grid;grid-template-columns:repeat(4,224px);gap:37px 28px;justify-content:center;margin-top:65px}
.staff-card{height:232px;background:var(--white);box-shadow:0 2px 14px rgba(0,0,0,.12);display:flex;flex-direction:column;align-items:center;padding-top:45px;font-size:17px;font-weight:500}
.staff-card .icon{width:100px;height:100px;border-radius:50%;background:var(--green);border:5px solid var(--white);box-shadow:0 0 0 2px #ddd;margin-bottom:24px}
.staff-card.is-active{background:var(--green);color:var(--white)}
.staff-card.is-active .icon{background:var(--white);box-shadow:0 0 0 2px #6a7457}

/* barriers */
.barriers{height:429px;background:var(--gold);color:var(--white);text-align:center;padding-top:50px}
.barriers h2{font-size:32px}
.barriers p{width:825px;margin:22px auto 0;font-size:15px;line-height:25.8px}
.barriers cite{display:block;font-style:normal;font-weight:700;font-size:15px;margin:20px 0 16px}

/* approach */
.approach{height:758px;padding-top:87px;text-align:center}
.approach-cols{display:flex;justify-content:center;gap:38px;margin-top:45px;align-items:flex-start}
.approach-col{width:296px;padding-top:30px}
.approach-col.is-featured{width:335px;height:368px;background:var(--white);border-radius:30px;box-shadow:0 4px 22px rgba(0,0,0,.12);border-bottom:6px solid var(--green);padding-top:22px;margin-top:4px}
.approach-col .icon{width:116px;height:116px;border-radius:50%;background:var(--gold);margin:0 auto 20px}
.is-featured .icon{background:var(--green)}
.approach-col h3{font-size:19px;font-weight:500;margin-bottom:12px}
.approach-col p{font-size:14px;line-height:24px;color:var(--text);padding:0 12px}
.read-more{display:inline-flex;align-items:center;gap:8px;margin-top:20px;font-size:13.5px;font-weight:500;text-transform:uppercase;color:var(--gold)}
.is-featured .read-more{color:var(--ink)}
.read-more svg{width:13px;height:13px}
.approach .btn{margin-top:54px;height:48px;padding:0 24px}

/* audience */
.audience{height:682px;background:var(--green-deep);color:var(--white);text-align:center;padding-top:80px}
.audience h2{font-size:32px}
.audience-cols{display:flex;justify-content:center;gap:34px;margin-top:30px}
.audience-col{width:302px}
.audience-photo{width:211px;height:211px;border-radius:50%;margin:0 auto 26px;border:2px solid #8c9478;padding:6px}
.audience-photo span{display:block;width:100%;height:100%;border-radius:50%}
.audience-col h3{font-size:15px;font-weight:700;margin-bottom:12px}
.audience-col p{font-size:14px;line-height:24px}
.audience-col .read-more{color:var(--white);font-weight:700}
.audience .btn{margin-top:34px;height:46px;background:var(--gold-soft)}

/* newsletter */
.newsletter{height:401px;background:var(--light);text-align:center;padding-top:87px}
.newsletter h2{font-size:32px;line-height:37px;color:var(--ink)}
.newsletter p{font-size:15px;margin-top:28px;font-weight:500}
.subscribe{display:flex;justify-content:center;gap:10px;margin-top:24px}
.field{width:378px;height:46px;background:var(--white);border:1px solid #ddd;border-radius:6px;display:flex;align-items:center;padding-left:20px;font-size:14px;color:#444}
.subscribe .btn{width:180px;justify-content:center;margin-left:2px}

/* footer */
.site-footer{position:relative;height:338px;padding:90px 0 0 114px;display:flex}
.footer-brand{width:359px}
.footer-brand .brand-name{font-size:52px}
.socials{display:flex;gap:8px;margin:26px 0 0 52px}
.socials span{width:31px;height:31px;border-radius:50%;background:var(--green)}
.footer-col h4{font-size:17px;font-weight:500;margin-bottom:22px}
.footer-col li{list-style:none;font-size:14px;line-height:26px;color:#333}
.quick{width:168px}
.misc{width:249px}
.contact li{display:flex;gap:12px;margin-bottom:14px;line-height:20px}
.contact li svg{width:14px;height:14px;flex:none;margin-top:3px}
.contact b{display:block;font-size:12px;font-weight:700}
.to-top{position:absolute;left:1128px;top:181px;width:36px;height:36px;border-radius:50%;background:var(--gold);display:flex;align-items:center;justify-content:center}
.copyright{height:59px;background:var(--gold);color:var(--white);font-size:15px;text-align:center;line-height:59px}
</style>
</head>
<body>

<svg width="0" height="0" style="position:absolute">
  <symbol id="arrow-circle" viewBox="0 0 16 16"><circle cx="8" cy="8" r="8" fill="currentColor"/><path d="M6 4.5 9.5 8 6 11.5" stroke="#fff" stroke-width="2" fill="none"/></symbol>
</svg>

<header class="site-header">
  <div class="brand"><span class="brand-name">CAMP 3874</span><span class="brand-mark"></span></div>
  <nav class="main-nav"><a>PROGRAMS</a><a>EVENTS</a><a>ONLINE STORE</a><a>ABOUT US</a><a>CONTACT US</a></nav>
  <a class="btn btn-gold signup">SIGN-UP</a>
</header>

<section class="hero" role="img" aria-label="Photo of two hikers trekking on a high mountain trail">
  <div class="hero-inner">
    <h1 class="heading">Empowering change: By illuminating lives<br>unexposed to the gospel's light</h1>
    <p>Camp 3874's mission is to enable the word of Jesus to be experienced by people in the most remote and treacherous parts of the world</p>
    <div class="hero-actions">
      <a class="btn btn-outline">View our programs <svg style="color:#fff"><use href="#arrow-circle"/></svg></a>
      <a class="btn btn-green">Register for training <svg style="color:#fff"><use href="#arrow-circle"/></svg></a>
    </div>
  </div>
</section>

<section class="staff">
  <h2 class="section-title heading">Camp 3874's well-rounded staff<br>for specialized training</h2>
  <div class="staff-grid">
    <div class="staff-card"><span class="icon" role="img" aria-label="Pastor icon"></span>PASTOR</div>
    <div class="staff-card"><span class="icon" role="img" aria-label="Nutritionist icon"></span>NUTRITIONIST</div>
    <div class="staff-card is-active"><span class="icon" role="img" aria-label="Dietician icon"></span>DIETICIAN</div>
    <div class="staff-card"><span class="icon" role="img" aria-label="Professional trainer icon"></span>PROFESSIONAL<br>TRAINER</div>
    <div class="staff-card"><span class="icon" role="img" aria-label="Former ranger icon"></span>FORMER RANGER</div>
    <div class="staff-card"><span class="icon" role="img" aria-label="Former special ops icon"></span>FORMER SPECIAL OPS</div>
    <div class="staff-card"><span class="icon" role="img" aria-label="Psychologist icon"></span>PSYCHOLOGIST</div>
    <div class="staff-card"><span class="icon" role="img" aria-label="Former special ops icon"></span>FORMER SPECIAL OPS</div>
  </div>
</section>

<section class="barriers">
  <h2 class="heading">Why Camp 3874 is breaking barriers</h2>
  <p>Geographical challenges make some communities difficult for missionaries to reach. The Camp 3874 program is designed to remove the physical limitations that can hinder us from bringing the Gospel to places that seem physically impossible to reach. Camp 3874 is founded on Romans 15:20. In his letter to the Romans, Paul requests funding to take the Gospel to Spain. In this letter, he writes: "[20] and thus I make it my ambition to preach the gospel, not where Christ has already been named, lest I build on someone else's foundation, [21] but it is written, "those who have never been told of him will see, and those who have never heard will understand.</p>
  <cite>(Romans 15:20-21)</cite>
  <a class="btn btn-green">Join our mission <svg style="color:#fff"><use href="#arrow-circle"/></svg></a>
</section>

<section class="approach">
  <h2 class="section-title heading">Camp 3874 missionary training approach<br>Mind - Body - Spirit</h2>
  <div class="approach-cols">
    <div class="approach-col">
      <div class="icon" role="img" aria-label="Mind icon"></div>
      <h3>Mind</h3>
      <p>Psychologically, we will prepare the mind through counseling, breathing techniques, and simulations in order to prepare for psychological challenges that come</p>
      <a class="read-more">Read more <svg><use href="#arrow-circle"/></svg></a>
    </div>
    <div class="approach-col is-featured">
      <div class="icon" role="img" aria-label="Body icon"></div>
      <h3>Body</h3>
      <p>Physically, we will prepare the body to overcome any physical limitations through rigorous exercises and nutritional coaching geared specifically to the geographical</p>
      <a class="read-more">Read more <svg><use href="#arrow-circle"/></svg></a>
    </div>
    <div class="approach-col">
      <div class="icon" role="img" aria-label="Spirit icon"></div>
      <h3>Spirit</h3>
      <p>Spiritually, we will prepare the soul to overcome spiritual challenges that arise in different areas of the world. Our curriculum is designed to prepare missionaries</p>
      <a class="read-more">Read more <svg><use href="#arrow-circle"/></svg></a>
    </div>
  </div>
  <a class="btn btn-green">View our detailed training program <svg style="color:#fff"><use href="#arrow-circle"/></svg></a>
</section>

<section class="audience">
  <h2 class="heading">Who is Camp 3874 for?</h2>
  <div class="audience-cols">
    <div class="audience-col">
      <div class="audience-photo"><span role="img" aria-label="Photo of a missionary sitting with a book" style="background:linear-gradient(160deg,#9aa1a6,#5c6a80 60%,#d9d2c4)"></span></div>
      <h3>Sending Agencies for Missionaries</h3>
      <p>Are you looking to improve the training you're offering your flock? We have designed a program to align our training with your goals</p>
      <a class="read-more">Read more <svg><use href="#arrow-circle"/></svg></a>
    </div>
    <div class="audience-col">
      <div class="audience-photo"><span role="img" aria-label="Photo of missionaries talking together outdoors" style="background:linear-gradient(160deg,#b9b2a3,#7d6f5e 55%,#a79a86)"></span></div>
      <h3>Missionaries</h3>
      <p>Are you independently seeking to develop your knowledge and skills independently? We are here to help! We can customize a training</p>
      <a class="read-more">Read more <svg><use href="#arrow-circle"/></svg></a>
    </div>
    <div class="audience-col">
      <div class="audience-photo"><span role="img" aria-label="Photo of hands folded in prayer over an open bible" style="background:linear-gradient(160deg,#3b2e24,#6b5141 55%,#cbbda6)"></span></div>
      <h3>Christian-based training program for ALL!</h3>
      <p>Are you looking to support the missionary community? Well we have a solution for you! We also offer a customized, personal</p>
      <a class="read-more">Read more <svg><use href="#arrow-circle"/></svg></a>
    </div>
  </div>
  <a class="btn btn-gold">View our training options <svg style="color:#fff"><use href="#arrow-circle"/></svg></a>
</section>

<section class="newsletter">
  <h2 class="heading">Join our missionary training: Stay up-to-date<br>on our training programs, missionary success<br>stories, and new program info</h2>
  <p>Subscribe and help us in supporting our missionaries as they spread the Gospel to all corners and areas of the world</p>
  <div class="subscribe">
    <div class="field">Enter Name</div>
    <div class="field">Enter Email</div>
    <a class="btn btn-gold">Subscribe now</a>
  </div>
</section>

<footer class="site-footer">
  <div class="footer-brand">
    <div class="brand"><span class="brand-name">CAMP 3874</span></div>
    <div class="socials"><span></span><span></span><span></span><span></span></div>
  </div>
  <div class="footer-col quick">
    <h4>Quick Links</h4>
    <ul><li>Programs</li><li>Events</li><li>Online Store</li><li>About Us</li><li>Contact Us</li></ul>
  </div>
  <div class="footer-col misc">
    <h4>Miscellaneous</h4>
    <ul><li>Terms of Service</li><li>Privacy Policy</li><li>Case Studies</li></ul>
  </div>
  <div class="footer-col contact">
    <h4>Contact Us</h4>
    <ul>
      <li><svg viewBox="0 0 14 14"><path d="M7 1a4 4 0 0 0-4 4c0 3 4 8 4 8s4-5 4-8a4 4 0 0 0-4-4z" fill="#e2b83b"/><circle cx="7" cy="5" r="1.5" fill="#fff"/></svg><div><b>Location</b>241,Lorem ipsum dolor amet<br>consectetur adipiscing elit,</div></li>
      <li><svg viewBox="0 0 14 14"><path d="M3 1l2.5 3-1.5 1.5a8 8 0 0 0 4.5 4.5L10 8.5l3 2.5-1.5 2C6 13 1 8 1 2.5z" fill="#e2b83b"/></svg><div><b>Phone</b>+888 888 8888</div></li>
      <li><svg viewBox="0 0 14 14"><rect x="1" y="3" width="12" height="8" rx="1" fill="#e2b83b"/><path d="M1 3.5 7 8l6-4.5" stroke="#fff" fill="none"/></svg><div><b>Email</b>info@camp3874.example</div></li>
    </ul>
  </div>
  <span class="to-top"><svg width="14" height="14" viewBox="0 0 14 14"><path d="M3 9l4-4 4 4" stroke="#2c3718" stroke-width="2" fill="none"/></svg></span>
</footer>
<div class="copyright">2023 Copyright - Camp 3874 | All Rights Reserved</div>

</body>
</html>
```